VALORINE NUTRACEUTICALS STORE

I have trademarked the Names VALORINE and QUESTAX. I currently have three products to sell on my store.
1.VALORINE CASCADE SUMMIT BLEND 60 Capsules.
2. VALORINE CASCADE SUMMIT BLEND 30 Grams
3. QUESTAX 60 Capsules
ALL REFERENCES ON THE WEB PAGE NEEDS TO HAVE THE TRADEMARK MARKS NEXT TO THE FOLLOWING WORDS WHEN THEY ARE PRINTED
CASCADE SUMMIT BLEND™
VALORINE®
QUESTAX®
(THOSE circled Rs are too big and should be in the upper right like it is with the TM)

I have the domain names Valorine.com and Questax.com. I would like both to lead to this store although the store name is valorine.com
I plan to start selling on tradora as well as other places as time progresses....
I have a number of pictures to populate my website with including three mockups and some others that will be uploaded. I would like the home page to have all three products featured with the prices straight forwardly presented.
1. above $23.95...
2. above $37.95
3. above. $32.95
Free standard NPDC Shipping , 5% discount off the entire order for any two products purchased, and 10% off the entire order for any 3 products purchased.
(Please note on the uploaded files there is a photo of the Cascade Summit Blend 30 Grams that has capsules next to the mockup bottle. ... Those capsules need to be removed from the mockup as the 30 gram bottle is pure powder not in capsules)
I have several files that show VALORINE NUTRACEUTICALS extracts are Highly Purified and 3rd Party tested (which is a major feature) These should have click access.
I did a little bit of work on the Shopify store but decided I needed a pro to work with

```html
<!DOCTYPE html>
<html lang="en">
<head>
<meta charset="utf-8">
<title>Valorine Nutraceuticals Store</title>
<link rel="stylesheet" href="https://fonts.googleapis.com/css2?family=Montserrat:wght@400;500;600;700;800&display=swap">
<style>
:root{
  --gold:#d9a84a;
  --gold-dark:#c8963a;
  --ink:#1c1b1b;
  --text:#222;
  --muted:#555;
  --card:#f5f3f3;
  --white:#fff;
  --night:#1f2447;
  --panel:rgba(62,60,60,.9);
}
*{margin:0;padding:0;box-sizing:border-box}
html,body{width:1200px;height:3883px;overflow:hidden;background:var(--white)}
body{font-family:"Montserrat",sans-serif;color:var(--text);position:relative}
sup{font-size:.5em;vertical-align:super;line-height:0}
.abs{position:absolute}
.btn{display:inline-block;background:var(--gold);color:var(--white);font-weight:700;text-transform:uppercase;letter-spacing:.02em;text-align:center}

/* header */
.site-header{left:0;top:0;width:1200px;height:80px;background:var(--white)}
.logo{left:133px;top:19px;font-size:34px;font-weight:800;color:var(--gold-dark);letter-spacing:.01em}
.main-nav{left:428px;top:34px;display:flex;gap:38px;font-size:13px;font-weight:500;color:#222}
.main-nav .active{color:var(--gold)}
.header-tools{left:942px;top:34px;display:flex;gap:12px;font-size:10px;align-items:center}
.header-tools span{display:flex;align-items:center;gap:5px}

/* hero */
.hero{left:0;top:80px;width:1200px;height:623px;background:linear-gradient(180deg,#131a3c 0%,#2b3a78 30%,#8d86b6 55%,#d9b9a4 66%,#574a34 78%,#2a2616 100%)}
.hero-title{left:0;top:66px;width:1200px;text-align:center;color:var(--white);font-size:38px;font-weight:800;line-height:48px;text-transform:uppercase}
.hero .btn{left:520px;top:233px;width:158px;height:51px;line-height:51px;font-size:19px}

/* products */
.product-card{top:737px;width:298px;height:441px;background:var(--card);text-align:center}
.product-shot{position:absolute;left:50px;top:30px;width:200px;height:270px;border-radius:6px;background:linear-gradient(160deg,#c9a24c 0%,#1f2033 18%,#2a2d52 60%,#171828 100%)}
.product-name{position:absolute;left:0;top:328px;width:100%;font-size:14.5px;line-height:24px;font-weight:500;color:#222}
.product-price{position:absolute;left:0;top:388px;width:100%;font-size:18px;font-weight:700;color:var(--gold)}

/* shipping band */
.shipping-band{left:130px;top:1205px;width:938px;height:116px;background:var(--ink);display:flex;align-items:center;justify-content:center;gap:30px}
.shipping-band p{color:var(--white);font-size:25px;font-weight:400}
.shipping-band .btn{width:170px;height:42px;line-height:42px;font-size:13px}

/* longevity banner */
.longevity{left:130px;top:1357px;width:938px;height:442px;background:linear-gradient(100deg,#cfd0cf 0%,#b3a8a6 35%,#e0dcdc 60%,#c6c3c5 100%)}
.longevity-panel{left:13px;top:155px;width:335px;height:275px;background:var(--panel);color:var(--white);padding:26px 32px}
.longevity-panel h2{font-size:17px;line-height:25px;font-weight:700;text-transform:uppercase}
.longevity-panel ul{list-style:none;margin-top:16px}
.longevity-panel li{font-size:17px;line-height:24px;display:flex;align-items:center;gap:12px}
.longevity-panel .btn{margin-top:22px;width:118px;height:36px;line-height:36px;font-size:14px}

/* duo offer */
.duo-photo{left:133px;top:1834px;width:455px;height:383px;background:linear-gradient(135deg,#5a5a5a,#1e1e1e 55%,#3a3a3a)}
.duo-offer{left:611px;top:1834px;width:455px;height:383px;background:var(--ink);color:var(--white);text-align:center}
.duo-offer p{position:absolute;left:0;top:97px;width:100%;font-size:21px;line-height:34px;font-weight:500;text-transform:uppercase}
.duo-offer .btn{position:absolute;left:161px;top:247px;width:126px;height:43px;line-height:43px;font-size:14px}

/* trio offer */
.trio-photo{left:0;top:2257px;width:672px;height:435px;background:linear-gradient(135deg,#e7c4c0 0%,#eef1fb 40%,#a6bde8 100%)}
.trio-offer{left:728px;top:2344px;color:#222}
.trio-offer p{font-size:30px;line-height:44px;font-weight:500;text-transform:uppercase}
.trio-offer .btn{margin-top:38px;width:126px;height:43px;line-height:43px;font-size:14px}

/* purity */
.purity{left:133px;top:2740px;width:935px;height:366px;background:linear-gradient(90deg,#e3b670 0%,#f3dca0 55%,#f6d98c 100%)}
.purity h2{position:absolute;left:70px;top:65px;font-size:26px;font-weight:600;color:#262626;text-transform:uppercase}
.purity p{position:absolute;left:71px;top:119px;width:380px;font-size:17.5px;line-height:26px;color:#333;text-transform:uppercase}
.purity .learn{position:absolute;left:72px;top:268px;width:127px;height:44px;line-height:44px;background:var(--white);color:var(--gold);font-size:14px;font-weight:700;text-align:center}
.purity-shot{position:absolute;left:560px;top:25px;width:330px;height:300px;border-radius:8px;background:linear-gradient(160deg,#c9a24c 0%,#1f2033 18%,#2a2d52 65%,#171828 100%)}

/* goals */
.goals-title{left:0;top:3153px;width:1200px;text-align:center;font-size:28px;font-weight:500;color:#222}
.goals-rule{left:564px;top:3203px;width:70px;height:2px;background:#444}
.goal{top:3242px;width:299px}
.goal .photo{height:226px}
.goal p{margin-top:35px;font-size:16px;font-weight:500;color:#222}

/* footer */
.site-footer{left:0;top:3559px;width:1200px;height:324px;background:var(--ink);color:var(--white)}
.site-footer h3{font-size:14px;font-weight:700;text-transform:uppercase}
.footer-about{left:131px;top:45px;width:300px}
.footer-about p{margin-top:14px;font-size:11.5px;line-height:17.5px;color:#ddd}
.footer-links{left:483px;top:45px}
.footer-links ul{list-style:none;margin-top:14px}
.footer-links li{font-size:11.5px;line-height:17.5px;color:#ddd;text-transform:uppercase}
.footer-news{left:655px;top:45px}
.footer-news p{margin-top:10px;font-size:12px;color:#ddd}
.signup{margin-top:18px;display:flex;width:413px;height:48px}
.signup span{flex:1;background:var(--white);color:#333;font-size:12px;line-height:48px;padding-left:18px}
.signup b{width:62px;background:var(--gold);display:flex;align-items:center;justify-content:center}
.copyright{left:131px;top:268px;font-size:12px;color:#eee}
.pay-cards{left:850px;top:263px;display:flex;gap:6px}
.pay-cards i{display:block;width:30px;height:19px;border-radius:3px;background:#e6e6e6}
</style>
</head>
<body>

<header class="site-header abs">
  <div class="logo abs">VALORINE®</div>
  <nav class="main-nav abs">
    <span class="active">HOME</span><span>ABOUT US</span><span>PRODUCTS</span><span>BLOG</span><span>CONTACT US</span>
  </nav>
  <div class="header-tools abs">
    <span><svg width="11" height="11" viewBox="0 0 12 12"><circle cx="5" cy="5" r="3.8" fill="none" stroke="#333" stroke-width="1.4"/><path d="M8 8l3 3" stroke="#333" stroke-width="1.4"/></svg>Account</span>
    <span><svg width="11" height="12" viewBox="0 0 11 12"><rect x="1" y="3.5" width="9" height="8" fill="none" stroke="#333" stroke-width="1.2"/><path d="M3.5 3.5V2.5a2 2 0 0 1 4 0v1" fill="none" stroke="#333" stroke-width="1.2"/></svg>Cart (0)</span>
  </div>
</header>

<section class="hero abs" role="img" aria-label="Man with arms outstretched in a grass field under a starry night sky">
  <h1 class="hero-title abs">VALORINE<sup>®</sup><br>Think Clearly - Stay Healthy<br>Be Immortal</h1>
  <a class="btn abs">Shop Now</a>
</section>

<article class="product-card abs" style="left:130px">
  <div class="product-shot" role="img" aria-label="Valorine Cascade Summit Blend 60 capsule bottle with capsules"></div>
  <div class="product-name">VALORINE<sup>®</sup><br>CASCADE SUMMIT BLEND<sup>™</sup> 60 Capsules</div>
  <div class="product-price">$23.95...</div>
</article>
<article class="product-card abs" style="left:449px">
  <div class="product-shot" role="img" aria-label="Valorine Cascade Summit Blend 30 gram powder bottle with scoop"></div>
  <div class="product-name">VALORINE<sup>®</sup><br>CASCADE SUMMIT BLEND<sup>™</sup> 30 Grams</div>
  <div class="product-price">$37.95</div>
</article>
<article class="product-card abs" style="left:768px">
  <div class="product-shot" role="img" aria-label="Questax NMN and resveratrol 60 capsule bottle with capsules"></div>
  <div class="product-name">QUESTAX<sup>®</sup><br>NMN &amp; RESVERATROL 60 Capsules</div>
  <div class="product-price">$32.95</div>
</article>

<section class="shipping-band abs">
  <p>Free standard NPDC Shipping</p>
  <a class="btn">Start Shopping</a>
</section>

<section class="longevity abs" role="img" aria-label="Athletic woman in a grey crop top resting by a bright window">
  <div class="longevity-panel abs">
    <h2>VALORINE<sup>®</sup> Affordable<br>Longevity Solutions</h2>
    <ul>
      <li><svg width="17" height="13" viewBox="0 0 17 13"><path d="M1.5 7l4.5 4.5L15.5 1.5" fill="none" stroke="#fff" stroke-width="2.6"/></svg>ANTI AGING</li>
      <li><svg width="17" height="13" viewBox="0 0 17 13"><path d="M1.5 7l4.5 4.5L15.5 1.5" fill="none" stroke="#fff" stroke-width="2.6"/></svg>NOOTROPIC</li>
      <li><svg width="17" height="13" viewBox="0 0 17 13"><path d="M1.5 7l4.5 4.5L15.5 1.5" fill="none" stroke="#fff" stroke-width="2.6"/></svg>SENOLYTIC</li>
      <li><svg width="17" height="13" viewBox="0 0 17 13"><path d="M1.5 7l4.5 4.5L15.5 1.5" fill="none" stroke="#fff" stroke-width="2.6"/></svg>ANTIOXIDANT</li>
    </ul>
    <a class="btn">Shop Now</a>
  </div>
</section>

<div class="duo-photo abs" role="img" aria-label="Smiling couple at a piano, man in a hat playing"></div>
<section class="duo-offer abs">
  <p>5% Discount off the<br>entire order for any<br>two products<br>purchased</p>
  <a class="btn">Shop Now</a>
</section>

<div class="trio-photo abs" role="img" aria-label="Three product bottles on a soft blue and pink light background"></div>
<section class="trio-offer abs">
  <p>10% off the<br>entire order for<br>any &nbsp;3 products<br>purchased.</p>
  <a class="btn">Shop Now</a>
</section>

<section class="purity abs">
  <h2>Whats inside the bottle</h2>
  <p>VALORINE<sup>®</sup> Nutraceuticals uses only the purest high potency extracts in our formulations. Our products are third pary tested to assure maximum purity.</p>
  <a class="learn">LEARN MORE</a>
  <div class="purity-shot" role="img" aria-label="Questax and Valorine bottles with capsules"></div>
</section>

<h2 class="goals-title abs">PRODUCT GOALS</h2>
<div class="goals-rule abs"></div>
<div class="goal abs" style="left:131px">
  <div class="photo" role="img" aria-label="Man with an axe in a forest" style="background:linear-gradient(135deg,#3e4a2c,#6b5a3a 50%,#2b3320)"></div>
  <p>Optimize Cellular Health</p>
</div>
<div class="goal abs" style="left:450px">
  <div class="photo" role="img" aria-label="Person on a peak above misty blue mountains" style="background:linear-gradient(180deg,#c8ced6,#8a97a8 60%,#3c4450)"></div>
  <p>Improve Mental Focus</p>
</div>
<div class="goal abs" style="left:769px">
  <div class="photo" role="img" aria-label="Smiling couple at a piano" style="background:linear-gradient(135deg,#5a5a5a,#1e1e1e 55%,#3a3a3a)"></div>
  <p>Increase Energy</p>
</div>

<footer class="site-footer abs">
  <div class="footer-about abs">
    <h3>About</h3>
    <p>There are many variations of passages of Lorem Ipsum available, but the majority have suffered alteration in some form, by injected humour, or randomised words which don't look even slightly believable.</p>
  </div>
  <div class="footer-links abs">
    <h3>Links</h3>
    <ul><li>Home</li><li>About Us</li><li>Products</li><li>Blog</li><li>Contact Us</li></ul>
  </div>
  <div class="footer-news abs">
    <h3>Stay Connected</h3>
    <p>Join our mailing list to get updates</p>
    <div class="signup"><span>Email Address</span><b><svg width="10" height="14" viewBox="0 0 10 14"><path d="M2 1.5l5.5 5.5L2 12.5" fill="none" stroke="#fff" stroke-width="2"/></svg></b></div>
  </div>
  <div class="copyright abs">Copyright © 2021 All Rights Reserved</div>
  <div class="pay-cards abs"><i></i><i></i><i></i><i></i><i></i><i></i></div>
</footer>

</body>
</html>
```